Disposable Mini Sauce Pot Design for Asian Chain Food Brands

We operate a Hainan Chicken Rice takeout brand under the name Wokly8, with our official website: www.Wokly8.com.
We offer four signature house sauces and are launching brand-new packaging for our sauce line. We require custom graphic designs exclusively for the sauce cup lids.
Product Material & Base Specs
The sauce cups are made of PP plastic, available in two translucent base options: Translucent White and Translucent Orange.
Four Sauce Varieties for Individual Lid Designs
1. Red Sauce – Fried Sweet Chili Sauce
2.Green Sauce – Scallion Oil Dressing
3.Sweet Soy Sauce
4.Sweet Red Sauce (Special for Fried Chicken)
Differentiate each sauce lid design through unique graphics, typography, or illustrative elements for easy customer identification.
The marking NET WT 2 OZ must be clearly printed on every lid.
**There is no need to print full descriptive text or the full name of the sauces on each lid; the design only needs to clearly differentiate the four sauce varieties.
**Please reference the original design style and brand color palette shown on our official website, and feel free to fully unleash your creativity.
Look and feel
Each slider illustrates characteristics of the customer's brand and the style your logo design should communicate.

```html
<!DOCTYPE html>
<html lang="en">
<head>
<meta charset="utf-8">
<title>Wokly8 Sauce Lids</title>
<link rel="stylesheet" href="https://fonts.googleapis.com/css2?family=Anton&family=Archivo+Black&family=Bebas+Neue&family=Roboto+Condensed:wght@500&display=swap">
<style>
  :root {
    --page: #ffffff;
    --cream: #f6f3f0;
    --orange: #f26f27;
    --orange-deep: #d95d24;
    --orange-shadow: #6e1f0c;
    --yellow: #ffe600;
    --green: #5cb800;
    --green-deep: #4f9f00;
    --green-shadow: #3d7c00;
    --red: #dc1515;
    --red-deep: #b9141a;
    --red-shadow: #7c0a12;
    --flame: #e4540e;
    --ink: #2a2626;
    --brown: #4e2a1e;
    --brown-deep: #3a221d;
    --brown-shadow: #2a1814;
    --mint: #5fe8c6;
  }
  * { box-sizing: border-box; margin: 0; padding: 0; }
  html, body { width: 1200px; height: 1200px; overflow: hidden; background: var(--page); }
  .sheet { position: relative; width: 1200px; height: 1200px; }

  .lid {
    position: absolute;
    width: 479px; height: 541px;
    border-radius: 62px;
    overflow: hidden;
    box-shadow: 4px 5px 6px rgba(0,0,0,.28);
  }
  .lid--chili   { left: 109px; top: 47px;  background: linear-gradient(135deg, var(--orange) 0%, var(--orange-deep) 55%, var(--orange) 100%); }
  .lid--scallion{ left: 612px; top: 47px;  background: linear-gradient(135deg, var(--green-deep) 0%, var(--green) 60%, var(--green-deep) 100%); }
  .lid--red     { left: 109px; top: 611px; background: linear-gradient(135deg, var(--red-deep) 0%, var(--red) 55%, var(--red-deep) 100%); }
  .lid--soy     { left: 612px; top: 611px; background: linear-gradient(135deg, var(--brown-deep) 0%, var(--brown) 60%, var(--brown-deep) 100%); }

  .flame {
    position: absolute; right: -20px; bottom: -30px;
    width: 170px; height: 220px;
    background: var(--flame);
    border-radius: 60% 40% 10% 10% / 70% 60% 10% 10%;
  }

  .brand {
    position: absolute; left: 0; right: 0; top: 40px;
    text-align: center;
    font-family: "Archivo Black", sans-serif;
    font-size: 34px; color: var(--cream);
    letter-spacing: 1px;
  }

  .line {
    position: absolute; left: 0; right: 0;
    text-align: center; white-space: nowrap; line-height: 1;
  }
  .title { transform: rotate(-3deg); position: absolute; inset: 0; }

  .net {
    position: absolute; left: 0; right: 0; bottom: 20px;
    text-align: center;
    font-family: "Roboto Condensed", sans-serif; font-weight: 500;
    font-size: 18px; color: var(--cream);
  }

  .tag {
    display: inline-block; padding: 2px 8px 0;
    font-family: "Archivo Black", sans-serif;
  }

  /* Fried sweet chili */
  .chili-fried { top: 118px; font-family: "Archivo Black", sans-serif; font-size: 94px; color: var(--cream); text-shadow: 6px 6px 0 var(--orange-shadow); letter-spacing: -2px; }
  .chili-sweet { top: 212px; font-family: "Archivo Black", sans-serif; font-size: 100px; color: var(--yellow); text-shadow: 6px 6px 0 var(--orange-shadow); letter-spacing: -2px; }
  .chili-chili { top: 318px; font-family: "Archivo Black", sans-serif; font-size: 98px; color: var(--cream); text-shadow: 6px 6px 0 var(--orange-shadow); letter-spacing: -2px; }
  .chili-sauce { top: 440px; }
  .chili-sauce .tag { background: var(--yellow); color: var(--orange); font-size: 36px; box-shadow: 5px 5px 0 var(--orange-shadow); }

  /* Scallion oil */
  .oil-scallion { top: 102px; font-family: "Bebas Neue", sans-serif; font-size: 124px; color: var(--cream); text-shadow: 5px 5px 0 var(--green-shadow); }
  .oil-oil { top: 192px; font-family: "Anton", sans-serif; font-size: 268px; color: var(--cream); text-shadow: 7px 7px 0 var(--green-shadow); letter-spacing: 4px; }
  .oil-dressing { top: 440px; }
  .oil-dressing .tag { background: var(--cream); color: var(--green); font-size: 36px; box-shadow: 5px 5px 0 var(--green-shadow); }

  /* Sweet red */
  .red-sweet { top: 110px; font-family: "Anton", sans-serif; font-size: 218px; color: var(--cream); text-shadow: 7px 7px 0 var(--red-shadow); transform: scaleX(.74); }
  .red-red { top: 292px; font-family: "Archivo Black", sans-serif; font-size: 168px; color: var(--cream); text-shadow: 7px 7px 0 var(--red-shadow); transform: scaleX(.88); letter-spacing: -4px; }
  .red-sauce { top: 438px; }
  .red-sauce .tag { background: var(--ink); color: var(--cream); font-size: 40px; }

  /* Sweet soy */
  .soy-sweet { top: 100px; font-family: "Anton", sans-serif; font-size: 190px; color: var(--mint); text-shadow: 6px 6px 0 var(--brown-shadow); transform: scaleX(.78); }
  .soy-soy { top: 262px; font-family: "Archivo Black", sans-serif; font-size: 232px; color: var(--cream); text-shadow: 7px 7px 0 var(--brown-shadow); transform: scaleX(.68); letter-spacing: -6px; }
  .soy-sauce { top: 436px; }
  .soy-sauce .tag { background: var(--mint); color: var(--brown); font-size: 40px; box-shadow: 5px 5px 0 var(--brown-shadow); }

  .spark { position: absolute; }
</style>
</head>
<body>
<main class="sheet">

  <section class="lid lid--chili" aria-label="Fried sweet chili sauce lid">
    <div class="brand">Wokly8</div>
    <svg class="spark" style="left:38px;top:104px" width="44" height="40" viewBox="0 0 44 40" aria-hidden="true">
      <path d="M14 2 L30 26 L24 28 Z M2 26 L22 36 L20 30 Z M36 14 L40 32 L34 30 Z" fill="var(--yellow)"/>
    </svg>
    <div class="title">
      <div class="line chili-fried">FRIED</div>
      <div class="line chili-sweet">SWEET</div>
      <div class="line chili-chili">CHILI</div>
      <div class="line chili-sauce"><span class="tag">SAUCE</span></div>
    </div>
    <div class="net">NET WT. 2 OZ</div>
  </section>

  <section class="lid lid--scallion" aria-label="Scallion oil dressing lid">
    <div class="brand">Wokly8</div>
    <svg class="spark" style="left:28px;top:100px" width="30" height="28" viewBox="0 0 30 28" aria-hidden="true">
      <circle cx="8" cy="20" r="6" fill="var(--cream)"/><circle cx="20" cy="6" r="4" fill="var(--cream)"/>
    </svg>
    <div class="title">
      <div class="line oil-scallion">SCALLION</div>
      <div class="line oil-oil">OIL</div>
      <div class="line oil-dressing"><span class="tag">DRESSING</span></div>
    </div>
    <div class="net">NET WT. 2 OZ</div>
  </section>

  <section class="lid lid--red" aria-label="Sweet red sauce lid">
    <div class="flame"></div>
    <div class="brand">Wokly8</div>
    <svg class="spark" style="left:32px;top:110px" width="36" height="40" viewBox="0 0 36 40" aria-hidden="true">
      <path d="M14 10 Q16 22 26 24 Q16 26 14 38 Q12 26 2 24 Q12 22 14 10Z M28 0 Q29 6 34 7 Q29 8 28 14 Q27 8 22 7 Q27 6 28 0Z" fill="var(--cream)"/>
    </svg>
    <svg class="spark" style="left:330px;top:430px" width="30" height="26" viewBox="0 0 30 26" aria-hidden="true">
      <path d="M18 6 Q19 14 28 15 Q19 16 18 24 Q17 16 8 15 Q17 14 18 6Z" fill="var(--yellow)"/>
    </svg>
    <svg class="spark" style="left:104px;top:470px" width="26" height="26" viewBox="0 0 26 26" aria-hidden="true">
      <path d="M10 6 Q11 14 20 15 Q11 16 10 24 Q9 16 0 15 Q9 14 10 6Z" fill="var(--yellow)"/>
    </svg>
    <div class="title">
      <div class="line red-sweet">SWEET</div>
      <div class="line red-red">RED</div>
      <div class="line red-sauce"><span class="tag">SAUCE</span></div>
    </div>
    <div class="net">NET WT. 2 OZ</div>
  </section>

  <section class="lid lid--soy" aria-label="Sweet soy sauce lid">
    <div class="brand">Wokly8</div>
    <svg class="spark" style="left:36px;top:110px" width="40" height="36" viewBox="0 0 40 36" aria-hidden="true">
      <circle cx="9" cy="9" r="8" fill="var(--mint)"/><circle cx="16" cy="30" r="5" fill="var(--mint)"/><circle cx="30" cy="16" r="3.5" fill="var(--mint)"/>
    </svg>
    <svg class="spark" style="left:110px;top:446px" width="30" height="30" viewBox="0 0 30 30" aria-hidden="true">
      <circle cx="8" cy="22" r="5" fill="var(--cream)"/><circle cx="22" cy="12" r="3" fill="var(--cream)"/>
    </svg>
    <svg class="spark" style="left:356px;top:420px" width="30" height="30" viewBox="0 0 30 30" aria-hidden="true">
      <circle cx="20" cy="8" r="5" fill="var(--cream)"/><circle cx="6" cy="20" r="3" fill="var(--cream)"/>
    </svg>
    <div class="title">
      <div class="line soy-sweet">SWEET</div>
      <div class="line soy-soy">SOY</div>
      <div class="line soy-sauce"><span class="tag">SAUCE</span></div>
    </div>
    <div class="net">NET WT. 2 OZ</div>
  </section>

</main>
</body>
</html>
```